Halvern Cards

Technical services company
Networking, EAS, access control, project management and consultation

Clean, bold, modern design Using existing company logo for colors

Include Facebook and twitter links, QR bar code?

Industry/Entity Type

It Company

Contact Information for Business Card

Halvern Technical Services
"Steadfastly devoted to your progress"
860-555-0147 Main

Derek Voslund
Managing Partner / President
derek.voslund@halvern-ts.example
860-555-0183 Direct
www.halvern-ts.example

```html
<!DOCTYPE html>
<html lang="en">
<head>
<meta charset="utf-8">
<title>Halvern Technical Services – Business Card</title>
<link rel="stylesheet" href="https://fonts.googleapis.com/css2?family=Caladea:wght@400;700&display=swap">
<style>
  :root {
    --card-blue: #45a6df;
    --brand-blue: #1f5fae;
    --white: #ffffff;
    --ink: #111418;
    --backdrop: #e4e6e8;
  }
  * { box-sizing: border-box; margin: 0; padding: 0; }
  html, body {
    width: 1200px; height: 1200px; overflow: hidden;
    background: var(--backdrop);
    font-family: "Caladea", Cambria, Georgia, serif;
  }
  .card {
    position: absolute; left: 150px; width: 900px; height: 514px;
    background: var(--card-blue);
    box-shadow: 0 4px 14px rgba(0,0,0,0.18);
    overflow: hidden;
  }
  .card--back { top: 70px; }
  .card--front { top: 616px; }

  /* Back: contact side */
  .rule-thin { position: absolute; left: 180px; top: 120px; width: 460px; height: 2px; background: var(--white); }
  .rule-thick { position: absolute; left: 100px; top: 222px; width: 530px; height: 4px; background: var(--white); }
  .holder { position: absolute; left: 200px; top: 134px; width: 460px; text-align: center; color: var(--ink); }
  .holder__name { font-size: 30px; font-weight: 700; letter-spacing: 0.5px; }
  .holder__title { font-size: 15px; font-weight: 700; margin-top: 4px; }

  .brand-box {
    position: absolute; left: 620px; top: 186px; width: 240px; height: 178px;
    background: var(--white);
    display: flex; flex-direction: column; align-items: center; justify-content: center; gap: 6px;
  }
  .brand-box__mark { width: 44px; height: 44px; border-radius: 50%; background: var(--brand-blue); }
  .brand-box__name { font-size: 18px; font-weight: 700; color: var(--brand-blue); text-align: center; line-height: 1.1; text-transform: uppercase; }
  .brand-box__tagline { font-size: 11px; font-weight: 700; color: var(--ink); }

  .contact-icons { position: absolute; left: 22px; top: 262px; display: flex; flex-direction: column; gap: 14px; }
  .contact-icons__item { width: 28px; height: 28px; background: var(--white); display: flex; align-items: center; justify-content: center; }
  .contact-list { position: absolute; left: 66px; top: 258px; list-style: none; color: var(--white); font-weight: 700; font-size: 23px; }
  .contact-list li { height: 42px; line-height: 32px; }

  .corner-squares { position: absolute; right: 40px; top: 360px; display: flex; flex-direction: column; gap: 18px; }
  .corner-squares span { width: 22px; height: 22px; background: var(--white); display: block; }

  /* Front: brand side */
  .panel {
    position: absolute; left: 60px; top: 60px; right: 60px; bottom: 60px;
    background: var(--white);
    box-shadow: inset 0 0 14px rgba(0,0,0,0.35);
    display: flex; flex-direction: column; align-items: center; justify-content: center;
  }
  .panel__mark { width: 120px; height: 120px; border-radius: 50%; background: var(--brand-blue); margin-bottom: 14px; }
  .panel__name { color: var(--brand-blue); font-weight: 700; text-align: center; line-height: 1; text-transform: uppercase; }
  .panel__name-main { display: block; font-size: 66px; letter-spacing: 1px; }
  .panel__name-sub { display: block; font-size: 34px; letter-spacing: 1px; margin-top: 4px; }
  .panel__tagline { margin-top: 10px; font-size: 16px; font-weight: 700; color: var(--ink); }
  .panel__underline { margin-top: 6px; width: 480px; height: 3px; background: linear-gradient(90deg, rgba(69,166,223,0), var(--card-blue), rgba(69,166,223,0)); }
</style>
</head>
<body>

<section class="card card--back" aria-label="Business card, contact side">
  <div class="rule-thin"></div>
  <div class="holder">
    <p class="holder__name">Derek Voslund</p>
    <p class="holder__title">Managing Partner / President</p>
  </div>
  <div class="rule-thick"></div>

  <div class="brand-box">
    <span class="brand-box__mark"></span>
    <p class="brand-box__name">Halvern<br>Technical Services</p>
    <p class="brand-box__tagline">Steadfastly devoted to your progress</p>
  </div>

  <div class="contact-icons" aria-hidden="true">
    <span class="contact-icons__item">
      <svg width="18" height="14" viewBox="0 0 18 14"><rect x="1" y="1" width="16" height="12" fill="none" stroke="#111418" stroke-width="1.5"/><path d="M1 1 L9 8 L17 1" fill="none" stroke="#111418" stroke-width="1.5"/></svg>
    </span>
    <span class="contact-icons__item">
      <svg width="14" height="18" viewBox="0 0 14 18"><rect x="2" y="1" width="10" height="16" rx="2" fill="#111418"/><rect x="4" y="3" width="6" height="8" fill="#ffffff"/></svg>
    </span>
    <span class="contact-icons__item">
      <svg width="18" height="18" viewBox="0 0 18 18"><circle cx="11" cy="7" r="5" fill="none" stroke="#111418" stroke-width="2"/><line x1="7.5" y1="10.5" x2="2" y2="16" stroke="#111418" stroke-width="2.5"/></svg>
    </span>
  </div>
  <ul class="contact-list">
    <li>derek.voslund@halvern-ts.example</li>
    <li>860-555-0183</li>
    <li>Direct- www.halvern-ts.example</li>
  </ul>

  <div class="corner-squares" aria-hidden="true"><span></span><span></span><span></span></div>
</section>

<section class="card card--front" aria-label="Business card, brand side">
  <div class="panel">
    <span class="panel__mark"></span>
    <p class="panel__name">
      <span class="panel__name-main">Halvern</span>
      <span class="panel__name-sub">Technical Services</span>
    </p>
    <p class="panel__tagline">Steadfastly devoted to your progress</p>
    <div class="panel__underline"></div>
  </div>
</section>

</body>
</html>
```